Bus Card and Materials for Handyman and Landscaping
RTCard and Material
Bus Card and Materials for Handyman and Landscaping - Construction
Creative Brief
Professional
RT Handymand and Landscaping
Owner
PO Box 8817 Hilo, Hawaii 96742
rtolen7819@mailbarrow.com
Insured
I'd like to use my business card also as a magnet for my car or yard signs. I like the colors but are also open to other colors that designers use through their creativity.
One side of the card with my information the other side for marketing purposes, logo or other images, designers - please continue to use your creativity to come up with stunning designs. Thank you
RTolen RTolen
Designers! Love the designs! I'd like to list the type of work I so on the back side or on the side of the card (use your creativity, its great!): Roof Restoration Cutting Trees Roofing Yard Maintenance Painting Yard Service (weekly, bi-monthly, monthly) Pressure Washing Extensions Building Restoration Drywall & Texture Concrete Work
Welcome designers! I'm excited to view your creative cutting edge designs for my business card, stationary, car magnet, and yard signs. Good luck to you all.

```html
<!DOCTYPE html>
<html lang="en">
<head>
<meta charset="utf-8">
<title>Makai Fix &amp; Yard – Business Card</title>
<link rel="stylesheet" href="https://fonts.googleapis.com/css2?family=Open+Sans:wght@400;600;700&family=Oswald:wght@700&display=swap">
<style>
  :root {
    --stage: #2b2b2e;
    --green-deep: #0d6a2b;
    --green-mid: #1a8a38;
    --green-light: #3fae4a;
    --black: #0b0b0b;
    --black-soft: #262626;
    --white: #ffffff;
    --island: #f3f5f3;
    --text-muted: #d9d9d9;
  }
  * { box-sizing: border-box; margin: 0; padding: 0; }
  html, body { width: 1200px; height: 795px; overflow: hidden; }
  body {
    background: var(--stage);
    font-family: "Open Sans", Arial, sans-serif;
    position: relative;
  }
  .card {
    position: absolute;
    top: 243px;
    width: 540px;
    height: 309px;
    border-radius: 4px;
    overflow: hidden;
    box-shadow: 0 14px 30px rgba(0,0,0,.45);
  }
  /* Front: contact side */
  .card-front {
    left: 45px;
    background: linear-gradient(160deg, var(--black-soft), var(--black) 60%);
  }
  .front-green {
    position: absolute; right: 0; top: 0;
    width: 50%; height: 100%;
    background: linear-gradient(180deg, var(--green-mid), var(--green-deep));
  }
  .island-map {
    position: absolute; left: 150px; top: 0;
    width: 390px; height: 309px;
  }
  .front-brand {
    position: absolute; left: 262px; top: 124px;
    width: 210px;
    display: flex; align-items: center; gap: 8px;
  }
  .brand-mark {
    width: 16px; height: 16px; flex: none;
    background: var(--green-mid);
  }
  .brand-name {
    font-family: "Oswald", Arial, sans-serif;
    font-weight: 700;
    font-size: 24px;
    line-height: 1.05;
    text-transform: uppercase;
    color: var(--green-deep);
    white-space: nowrap;
  }
  .contact {
    position: absolute; left: 26px; bottom: 26px;
    color: var(--white);
  }
  .contact-name { font-size: 20px; font-weight: 700; }
  .contact-role { font-size: 12px; color: var(--text-muted); margin-bottom: 18px; }
  .contact-line {
    font-size: 12px; line-height: 1.6;
    display: flex; align-items: center; gap: 6px;
  }
  .contact-line svg { width: 11px; height: 11px; fill: var(--white); }

  /* Back: services side */
  .card-back {
    left: 615px;
    background: radial-gradient(ellipse at 55% 40%, var(--green-light), var(--green-mid) 45%, var(--green-deep));
    color: var(--white);
  }
  .back-brand {
    position: absolute; left: 0; right: 0; top: 70px;
    display: flex; justify-content: center; align-items: center; gap: 12px;
  }
  .back-brand .brand-mark { width: 22px; height: 22px; background: var(--white); }
  .back-brand .brand-name { color: var(--white); font-size: 40px; }
  .back-tagline {
    position: absolute; left: 0; right: 0; top: 128px;
    text-align: center; font-size: 11px; letter-spacing: 3px;
    text-transform: uppercase;
  }
  .services {
    position: absolute; left: 0; right: 0; bottom: 38px;
    list-style: none; text-align: center;
    font-size: 13px; line-height: 1.75;
  }
</style>
</head>
<body>

<section class="card card-front" aria-label="Business card, contact side">
  <div class="front-green"></div>
  <svg class="island-map" viewBox="0 0 390 309" role="img" aria-label="White silhouette of the island of Hawaii">
    <path d="M60 0 L330 0 C340 40 360 60 390 70 L390 150 C350 170 340 220 300 250 C260 280 200 300 150 309 L120 309 C110 270 80 250 40 240 C15 200 0 160 10 120 C30 80 50 40 60 0 Z" fill="var(--island)"/>
  </svg>
  <div class="front-brand">
    <span class="brand-mark"></span>
    <span class="brand-name">Makai Fix &amp; Yard</span>
  </div>
  <div class="contact">
    <p class="contact-name">Ray Tolen</p>
    <p class="contact-role">Owner</p>
    <p class="contact-line">PO Box 8817</p>
    <p class="contact-line">Hilo, Hawaii 96742</p>
    <p class="contact-line">
      <svg viewBox="0 0 24 24" aria-hidden="true"><path d="M6.6 10.8a15 15 0 0 0 6.6 6.6l2.2-2.2c.3-.3.7-.4 1-.2 1.1.4 2.3.6 3.6.6.6 0 1 .4 1 1V20c0 .6-.4 1-1 1A17 17 0 0 1 3 4c0-.6.4-1 1-1h3.5c.6 0 1 .4 1 1 0 1.3.2 2.5.6 3.6.1.3 0 .7-.2 1z"/></svg>
      808-555-0147
    </p>
    <p class="contact-line">
      <svg viewBox="0 0 24 24" aria-hidden="true"><path d="M2 5h20v14H2z M4 7v.5l8 5 8-5V7l-8 5z" fill-rule="evenodd"/></svg>
      rtolen7819@mailbarrow.com
    </p>
    <p class="contact-line">www.makaifixyard.com</p>
  </div>
</section>

<section class="card card-back" aria-label="Business card, services side">
  <div class="back-brand">
    <span class="brand-mark"></span>
    <span class="brand-name">Makai Fix &amp; Yard</span>
  </div>
  <p class="back-tagline">Honest Work, Fair Price</p>
  <ul class="services">
    <li>Roof Restoration • Cutting Trees • Roofing Yard Maintenance</li>
    <li>Painting Yard Service (weekly, bi-monthly, monthly) • Pressure Washing</li>
    <li>Extensions Building Restoration • Drywall &amp; Texture • Concrete Work</li>
  </ul>
</section>

</body>
</html>
```